Wild Over Gadgets: Fun, Clean Website Banner Design!

Wild Over Gadgets is passionate about bringing the world of science to all young Australians, and making it FUN!

We need a new website banner designed for our website www.wildovergadgets.com.au

We need two versions of the same banner - one with some Christmas embellishments and one without.

The banner should be eye-catching, clean and professional looking. It should fit in with our website page design. See our existing sliding banner designs to get an idea of the look and feel at www.wildovergadgets.com.au

It should include some text, a background image for context (perhaps a desk?) or graphic element, a call to action button, as well as some images of desktop toys we sell, see attached. Not all have to be included. The call to action button is BROWSE ALL ITEMS.

The banner measures 1102 x 415 px

Banner Text:
Desktop Science
Curiosities for your desk or classroom

Target Market(s)

Parents of curious kids, science enthusiasts and teachers

Contact Information for Business Card

Include logo (attached image), some samples of singage we've had designed are attached for inspiration. Would be open to single or double sided design.
Feel is modern sophisticated, modern, progressive, eye-cathcing. Balance between seious and fun to appeal to all segments of our market - serious schools as well as fun for kids.
May not include dots, as trying to mature from too young and silly.
Text detail to include:
Name
Position
Seriously Fun!
www.wildovergadgets.com.au
name@wildovergadgets.com.au
2B/476 Harlow Rd, Kelverton, VIC, 3928
1300 417 286
Fax: 03 7514 3982

Science Shop
School Workshops
Parties & Events
Lab Supplies & Teacher Resources

Font styles to use
Sans Serif

Requirements
Must have
• We need two versions of the same banner - one with Christmas embellishments and one without.
• Images of desktop toys we sell, see attached. Not all have to be included.
• Call to action button BROWSE ALL ITEMS.
• Banner Text:
• Desktop Science
• Curiosities for your desk or classroom
Nice to have
• A background image for context such as a desk? or a graphic element
Should not have
• Fun and exciting, but not too young and immature.

```html
<!DOCTYPE html>
<html lang="en">
<head>
<meta charset="utf-8">
<title>Desktop Science – Banner Set</title>
<link rel="stylesheet" href="https://fonts.googleapis.com/css2?family=Open+Sans:wght@600;700&family=PT+Sans+Narrow:wght@700&display=swap">
<style>
  :root {
    --board-dark: #1c1d21;
    --board-mid: #2c2e33;
    --green-deep: #0b6a52;
    --green-bright: #2fd6b6;
    --red-deep: #7e1220;
    --red-bright: #dd452b;
    --teal: #1f9c8c;
    --navy: #0a1a2b;
    --shelf-top: #6f7174;
    --shelf-light: #8a8c8f;
    --shelf-edge: #4b4d50;
    --shelf-lip: #9a9184;
    --title: #ffffff;
    --button-top: #ffd23a;
    --button-bottom: #f2a400;
    --button-text: #2a1a00;
  }
  * { box-sizing: border-box; margin: 0; padding: 0; }
  html, body { width: 768px; height: 1200px; overflow: hidden; }
  body {
    background: radial-gradient(ellipse at 50% 100%, var(--board-mid), var(--board-dark) 70%);
    font-family: "Open Sans", Arial, sans-serif;
    position: relative;
  }
  .banner {
    position: absolute;
    left: 63px;
    width: 643px;
    height: 241px;
    overflow: hidden;
  }
  .banner--one { top: 90px; }
  .banner--two { top: 349px; }
  .banner--three { top: 609px; }
  .banner--four { top: 868px; }

  .banner__sky { position: absolute; inset: 0 0 95px 0; }
  .banner--one .banner__sky { background: linear-gradient(100deg, var(--green-deep) 0%, #149a7e 45%, var(--green-bright) 75%, #1fa88c 100%); }
  .banner--two .banner__sky { background: linear-gradient(100deg, var(--red-deep) 0%, #b2241f 45%, var(--red-bright) 75%, #c4311f 100%); }
  .banner--three .banner__sky { background: linear-gradient(100deg, var(--red-deep) 0%, #b2241f 40%, #d23a22 75%, #c32e1c 100%); }
  .banner--four .banner__sky { background: linear-gradient(100deg, var(--teal) 0%, #2bb5a2 30%, #135a6a 60%, var(--navy) 100%); }

  .banner__glow {
    position: absolute; left: 0; top: 0; width: 643px; height: 146px;
    background: radial-gradient(ellipse 70% 18% at 35% 88%, rgba(255,255,255,0.55), rgba(255,255,255,0) 70%);
  }

  .banner__decor { position: absolute; }
  .banner__decor--wreath {
    right: 0; top: 0; width: 190px; height: 150px;
    background: radial-gradient(ellipse at 60% 40%, rgba(0,0,0,0.18), rgba(0,0,0,0) 70%);
  }
  .banner__decor--gifts {
    left: 410px; top: 18px; width: 210px; height: 112px;
    background: radial-gradient(ellipse at 50% 55%, rgba(90,10,10,0.22), rgba(0,0,0,0) 70%);
  }

  .banner__shelf {
    position: absolute; left: 0; right: 0; top: 146px; height: 83px;
    background: linear-gradient(180deg, var(--shelf-light) 0%, var(--shelf-top) 30%, #606265 100%);
  }
  .banner__shelf-edge {
    position: absolute; left: 0; right: 0; top: 229px; height: 8px;
    background: linear-gradient(180deg, var(--shelf-edge), #5d5f62);
  }
  .banner__shelf-lip {
    position: absolute; left: 0; right: 0; top: 237px; height: 4px;
    background: var(--shelf-lip);
  }

  .banner__title {
    position: absolute; left: 29px; top: 8px;
    color: var(--title);
    font-weight: 700;
    font-size: 40px;
    letter-spacing: -0.5px;
    line-height: 1;
    text-shadow: 0 1px 2px rgba(0,0,0,0.25);
  }
  .banner__tagline {
    position: absolute; left: 30px; top: 50px;
    color: var(--title);
    font-weight: 600;
    font-size: 13.4px;
    letter-spacing: 1.4px;
    line-height: 1;
  }

  .product { position: absolute; border-radius: 6px; }
  .product--orbs { left: 21px; top: 74px; width: 96px; height: 124px;
    background: radial-gradient(ellipse at 50% 45%, #b9a7c8, #5a4b66 55%, rgba(30,30,30,0.9) 100%); }
  .product--engine { left: 133px; top: 62px; width: 80px; height: 136px;
    background: linear-gradient(180deg, #e0a24a 0%, #c98a2f 55%, #8e8a80 80%, #2e3236 100%); }
  .product--sandframe { left: 248px; top: 88px; width: 96px; height: 108px; border-radius: 48px 48px 6px 6px;
    background: radial-gradient(circle at 50% 42%, #ffffff 0%, #a9cdea 35%, #2f77b7 62%, #2b2e32 72%); }
  .product--atom { left: 393px; top: 74px; width: 77px; height: 126px;
    background: radial-gradient(ellipse at 45% 40%, #c04a3a 0%, #5564a8 35%, #2a2c30 80%); }

  .cta {
    position: absolute; left: 497px; top: 170px;
    width: 128px; height: 30px;
    border-radius: 5px;
    background: linear-gradient(180deg, var(--button-top), var(--button-bottom));
    box-shadow: 0 2px 3px rgba(0,0,0,0.35);
    display: flex; align-items: center;
    padding-left: 8px;
    font-family: "PT Sans Narrow", "Arial Narrow", sans-serif;
    font-weight: 700; font-size: 12.5px;
    color: var(--button-text);
    text-decoration: none;
  }
  .banner--four .cta { left: 494px; top: 175px; }
  .cta__divider { position: absolute; left: 102px; top: 4px; width: 1px; height: 22px; background: rgba(80,50,0,0.4); }
  .cta__arrows { position: absolute; left: 107px; top: 8px; width: 15px; height: 14px; }
</style>
</head>
<body>

<section class="banner banner--one">
  <div class="banner__sky"></div>
  <div class="banner__decor banner__decor--wreath" role="img" aria-label="Christmas wreath with pine cones and bells"></div>
  <div class="banner__shelf"></div>
  <div class="banner__shelf-edge"></div>
  <div class="banner__shelf-lip"></div>
  <h1 class="banner__title">DESKTOP SCIENCE</h1>
  <p class="banner__tagline">CURIOSITIES FOR YOUR DESK OR CLASSROOM</p>
  <div class="product product--orbs" role="img" aria-label="Perpetual motion orb desk toy"></div>
  <div class="product product--engine" role="img" aria-label="Brass Stirling engine"></div>
  <div class="product product--sandframe" role="img" aria-label="Round moving sand picture"></div>
  <div class="product product--atom" role="img" aria-label="Spinning atom model on stand"></div>
  <a class="cta" href="#">BROWSE ALL ITEMS<span class="cta__divider"></span>
    <svg class="cta__arrows" viewBox="0 0 15 14"><path d="M1 1l6 6-6 6M7 1l6 6-6 6" fill="none" stroke="#2a1a00" stroke-width="2.2"/></svg></a>
</section>

<section class="banner banner--two">
  <div class="banner__sky"></div>
  <div class="banner__decor banner__decor--wreath" role="img" aria-label="Christmas wreath with pine cones and bells"></div>
  <div class="banner__shelf"></div>
  <div class="banner__shelf-edge"></div>
  <div class="banner__shelf-lip"></div>
  <h1 class="banner__title">DESKTOP SCIENCE</h1>
  <p class="banner__tagline">CURIOSITIES FOR YOUR DESK OR CLASSROOM</p>
  <div class="product product--orbs" role="img" aria-label="Perpetual motion orb desk toy"></div>
  <div class="product product--engine" role="img" aria-label="Brass Stirling engine"></div>
  <div class="product product--sandframe" role="img" aria-label="Round moving sand picture"></div>
  <div class="product product--atom" role="img" aria-label="Spinning atom model on stand"></div>
  <a class="cta" href="#">BROWSE ALL ITEMS<span class="cta__divider"></span>
    <svg class="cta__arrows" viewBox="0 0 15 14"><path d="M1 1l6 6-6 6M7 1l6 6-6 6" fill="none" stroke="#2a1a00" stroke-width="2.2"/></svg></a>
</section>

<section class="banner banner--three">
  <div class="banner__sky"></div>
  <div class="banner__decor banner__decor--gifts" role="img" aria-label="Line drawing of wrapped gift boxes"></div>
  <div class="banner__shelf"></div>
  <div class="banner__shelf-edge"></div>
  <div class="banner__shelf-lip"></div>
  <h1 class="banner__title">DESKTOP SCIENCE</h1>
  <p class="banner__tagline">CURIOSITIES FOR YOUR DESK OR CLASSROOM</p>
  <div class="product product--orbs" role="img" aria-label="Perpetual motion orb desk toy"></div>
  <div class="product product--engine" role="img" aria-label="Brass Stirling engine"></div>
  <div class="product product--sandframe" role="img" aria-label="Round moving sand picture"></div>
  <div class="product product--atom" role="img" aria-label="Spinning atom model on stand"></div>
  <a class="cta" href="#">BROWSE ALL ITEMS<span class="cta__divider"></span>
    <svg class="cta__arrows" viewBox="0 0 15 14"><path d="M1 1l6 6-6 6M7 1l6 6-6 6" fill="none" stroke="#2a1a00" stroke-width="2.2"/></svg></a>
</section>

<section class="banner banner--four">
  <div class="banner__sky"></div>
  <div class="banner__glow"></div>
  <div class="banner__shelf"></div>
  <div class="banner__shelf-edge"></div>
  <div class="banner__shelf-lip"></div>
  <h1 class="banner__title">DESKTOP SCIENCE</h1>
  <p class="banner__tagline">CURIOSITIES FOR YOUR DESK OR CLASSROOM</p>
  <div class="product product--orbs" role="img" aria-label="Perpetual motion orb desk toy"></div>
  <div class="product product--engine" role="img" aria-label="Brass Stirling engine"></div>
  <div class="product product--sandframe" role="img" aria-label="Round moving sand picture"></div>
  <div class="product product--atom" role="img" aria-label="Spinning atom model on stand"></div>
  <a class="cta" href="#">BROWSE ALL ITEMS<span class="cta__divider"></span>
    <svg class="cta__arrows" viewBox="0 0 15 14"><path d="M1 1l6 6-6 6M7 1l6 6-6 6" fill="none" stroke="#2a1a00" stroke-width="2.2"/></svg></a>
</section>

</body>
</html>
```